Tolvene Hub Redesign

tolvenehub.com is one of our old, high-traffic multilingual site.

its interface is very old, so we want to redesign it to give a modern, attractive design, with comfortable colors and layout.

beside the current content of the main page we want to add two places for dynamic banners.

The site has an App in iOS and Droidline, we want an ad in a noticeable place for it.

this ad will be permanent.

the site now has 12 languages, but we may add new languages soon, so design must consider this.

redesign of two internal pages also required:
- the main listing page, example: http://www.tolvenehub.example/en/cat/252
- the article view page: http://www.tolvenehub.example/en/10323

Reason: want to receive more designs ...

```html
<!DOCTYPE html>
<html lang="en">
<head>
<meta charset="utf-8">
<title>Tolvene Hub — Question &amp; Answer</title>
<link href="https://fonts.googleapis.com/css2?family=Arimo:wght@400;700&family=Lato:wght@400;700&display=swap" rel="stylesheet">
<style>
:root{
  --ink:#2b2b2b;
  --ink-soft:#3a3a3a;
  --muted:#6d6d6d;
  --rule:#c9c9c9;
  --accent:#8a4a2a;
  --pill:#3b3e41;
  --panel-top:#4a4e52;
  --panel:#2e3134;
  --panel-text:#f2f2f2;
  --parch-1:#f0dfba;
  --parch-2:#e2c894;
  --band-1:#a5875d;
  --band-2:#d8c29a;
  --ios-1:#7c8186;
  --ios-2:#5f6468;
  --droid-1:#b4d23a;
  --droid-2:#93bb22;
}
*{box-sizing:border-box;margin:0;padding:0}
html,body{width:1200px;height:1026px;overflow:hidden;background:#fff}
body{position:relative;font-family:Arimo,Arial,sans-serif;color:var(--ink)}
.abs{position:absolute}

/* header */
.brand{left:180px;top:24px;display:flex;align-items:center;gap:8px}
.brand-dot{width:16px;height:16px;border-radius:50%;background:#c2388d}
.brand-name{font-family:Lato,sans-serif;font-weight:700;font-size:31px;color:var(--ink);line-height:1}
.brand-tag{left:192px;top:64px;font-family:Lato,sans-serif;font-size:11.5px;color:var(--ink-soft)}

.social{top:11px;left:772px;display:flex;gap:4px}
.social span{width:14px;height:14px;border-radius:50%;background:#c7c9cc}
.social span:nth-child(2){background:#8cc63f}
.lang{left:844px;top:11px;width:166px;height:15px;border:1px solid #d4d4d4;border-radius:8px;display:flex;align-items:center;font-size:8.5px}
.lang b{background:var(--pill);color:#fff;border-radius:8px;height:15px;line-height:15px;padding:0 7px;margin:-1px 0 0 -1px}
.lang em{font-style:normal;color:#888;margin-left:7px;flex:1}
.lang i{border:3px solid transparent;border-top:4px solid #888;margin:3px 8px 0 0}

.date{left:581px;top:37px;font-size:8.5px;color:var(--ink-soft);padding-right:8px;border-right:1px solid #555;line-height:14px}
.search{left:736px;top:34px;width:274px;height:16px;border:1px solid #d4d4d4;border-radius:8px;display:flex;align-items:center;font-size:8.5px}
.search b{background:var(--pill);color:#fff;border-radius:8px;height:16px;line-height:16px;padding:0 7px;margin:-1px 0 0 -1px}
.search em{font-style:normal;color:#999;margin-left:7px;flex:1}
.search svg{margin-right:6px}

.nav{top:66px;left:537px;display:flex;font-size:12px}
.nav a{color:var(--ink);text-decoration:none;height:14px;line-height:14px;margin-right:13px}
.nav a.current{background:var(--pill);color:#fff;padding:0 5px;border-radius:2px;margin-right:14px}
.rule-top{left:182px;top:90px;width:836px;height:1px;background:var(--rule)}

/* slider */
.slider{left:182px;top:106px;width:836px;height:270px;overflow:hidden}
.slider-shadow{left:160px;top:360px;width:890px;height:30px;border-radius:50%;background:radial-gradient(ellipse at center,rgba(0,0,0,.35),rgba(0,0,0,0) 70%)}
.parchment{inset:0;background:radial-gradient(ellipse at 40% 50%,var(--parch-1),var(--parch-2))}
.band{left:0;width:836px;height:26px;background:linear-gradient(180deg,var(--band-1),var(--band-2) 50%,var(--band-1))}
.band.top{top:0}.band.bottom{bottom:0;height:32px}
.photo{left:542px;top:38px;width:294px;height:198px;background:linear-gradient(120deg,#f4efe0 0%,#e7dcc2 45%,#c89a78 75%,#ece9e4 100%)}
.slide-title{left:48px;top:82px;font-family:Lato,sans-serif;font-weight:400;font-size:34px;line-height:38px;color:var(--ink-soft)}
.slide-text{left:49px;top:124px;width:300px;font-size:10px;line-height:12px;color:#222}
.read-more{left:48px;top:167px;height:14px;line-height:14px;padding:0 8px;border-radius:7px;background:var(--pill);color:#fff;font-size:8.5px;font-weight:700}
.dots{left:393px;top:207px;display:flex;gap:7px}
.dots span{width:12px;height:12px;border-radius:50%;background:#2c2c2c;border:2px solid #2c2c2c}
.dots span.on{background:#fff}
.arrow{top:118px}

/* apps */
.app{left:182px;width:156px;height:128px;border-radius:5px;overflow:hidden;color:#fff}
.app.ios{top:393px;background:linear-gradient(180deg,var(--ios-1),var(--ios-2))}
.app.droid{top:536px;height:127px;background:linear-gradient(180deg,var(--droid-1),var(--droid-2))}
.app-copy{position:absolute;left:37px;top:9px;white-space:nowrap}
.app-copy small{display:block;font-size:8px;line-height:10px}
.app-copy strong{display:block;font-family:Lato,sans-serif;font-size:24px;line-height:26px;font-weight:700}
.app-icon{position:absolute;left:10px;top:11px;width:18px;height:30px;border:3px solid #fff;border-radius:3px}
.app-art{position:absolute;left:20px;top:54px;width:116px;height:60px;border-radius:6px}
.app.ios .app-art{background:linear-gradient(180deg,rgba(255,255,255,.28),rgba(255,255,255,.08))}
.app.droid .app-art{background:linear-gradient(180deg,rgba(255,255,255,.3),rgba(255,255,255,.08))}

/* fatwas */
.fatwas{top:388px;width:311px}
.fatwas h2{font-size:17px;font-weight:700;color:var(--ink-soft);padding-bottom:4px;border-bottom:1px solid #9a9a9a}
.fatwas ul{list-style:none;margin-top:10px}
.fatwas li{font-size:8.6px;line-height:13.6px;margin-bottom:13.6px;padding-left:1px}
.fatwas li::before{content:"• "}
.fatwas li.hl{color:var(--accent)}

/* tab panels */
.tabs{top:705px;display:flex;gap:8px;align-items:flex-end}
.tab{background:var(--panel-top);color:#fff;border-radius:5px 5px 0 0;height:28px;display:flex;align-items:center;justify-content:center}
.tab.big{font-size:14px}
.tab.small{font-size:9.5px;line-height:10px;padding:0 8px}
.tab.active{font-weight:700}
.panel{top:732px;width:410px;height:233px;border-radius:0 0 5px 5px;background:linear-gradient(180deg,var(--panel-top),var(--panel) 40px);color:var(--panel-text)}
.panel ul{list-style:none;padding:16px 0 0 19px;font-size:9.6px}
.panel li{line-height:21px}
.panel li::before{content:"• "}
.panel.right ul{padding-right:18px}

/* footer */
.rule-foot{left:182px;top:987px;width:836px;height:1px;background:#a0a0a0}
.footer{left:181px;top:994px;font-size:9.5px;color:var(--ink-soft)}
</style>
</head>
<body>

<header>
  <div class="abs brand"><span class="brand-dot"></span><span class="brand-name">Tolvene Hub</span></div>
  <div class="abs brand-tag">Question &amp; Answer</div>

  <div class="abs social" aria-label="App and social links"><span></span><span></span><span></span><span></span></div>
  <div class="abs lang"><b>Select Language</b><em>English</em><i></i></div>

  <div class="abs date">Thu 26 DhH 1434 - 31 October 2013</div>
  <div class="abs search"><b>Advanced</b><em>Search Key Word</em>
    <svg width="11" height="11" viewBox="0 0 11 11"><circle cx="4.5" cy="4.5" r="3.5" fill="none" stroke="#333" stroke-width="1.5"/><line x1="7" y1="7" x2="10" y2="10" stroke="#333" stroke-width="1.8"/></svg>
  </div>

  <nav class="abs nav">
    <a class="current" href="#">Home</a><a href="#">Categories</a><a href="#">New Fatwas</a><a href="#">About</a><a href="#">Send A Question</a><a href="#">Indtroduction to Islam</a>
  </nav>
  <div class="abs rule-top"></div>
</header>

<div class="abs slider-shadow"></div>
<section class="abs slider">
  <div class="abs parchment" role="img" aria-label="Cream parchment background with faint floral pattern"></div>
  <div class="abs band top" role="img" aria-label="Carved arabesque border"></div>
  <div class="abs band bottom" role="img" aria-label="Carved arabesque border"></div>
  <div class="abs photo" role="img" aria-label="Photo of a hand holding an open book"></div>
  <h1 class="abs slide-title">Tolvene Hub</h1>
  <p class="abs slide-text">Lorem Ipsum has been the industry's standard dummy text ever since the 1500s, when an unknown printer took a galley of type and scrambled it to make a type specimen book.</p>
  <span class="abs read-more">Read More</span>
  <div class="abs dots"><span class="on"></span><span></span><span></span></div>
  <svg class="abs arrow" style="left:14px" width="20" height="34" viewBox="0 0 20 34"><polyline points="17,2 3,17 17,32" fill="none" stroke="#2b2b2b" stroke-width="1.6"/></svg>
  <svg class="abs arrow" style="left:802px" width="20" height="34" viewBox="0 0 20 34"><polyline points="3,2 17,17 3,32" fill="none" stroke="#2b2b2b" stroke-width="1.6"/></svg>
</section>

<aside>
  <div class="abs app ios">
    <span class="app-icon"></span>
    <div class="app-copy"><small>Available on the Pocketphone</small><strong>App Shelf</strong></div>
    <div class="app-art" role="img" aria-label="Promotional artwork area for the phone app"></div>
  </div>
  <div class="abs app droid">
    <span class="app-icon"></span>
    <div class="app-copy"><small>Available on the Droidline</small><strong>App Shelf</strong></div>
    <div class="app-art" role="img" aria-label="Promotional artwork area for the phone app"></div>
  </div>
</aside>

<section class="abs fatwas" style="left:366px">
  <h2>New Fatwas</h2>
  <ul>
    <li>He works as a nurse, which means that he may do some things that are not acceptable according to sharee'ah.</li>
    <li class="hl">Her mother wants her to marry one suitor, but her father thinks that he is not suitable; what should she do?.</li>
    <li>Her mother wants her to marry one suitor, but her father thinks that he is not suitable; what should she do?.</li>
    <li class="hl">Raising Muslim children in the West to have an aversion to pigs.</li>
    <li>His parents think that he does not offer the naafil prayers, but he prays them in secret for fear of showing off. Should he tell them about that?.</li>
    <li class="hl">Some of the signs of puberty appeared in her daughters at the age of six; what should she do?.</li>
  </ul>
</section>
<section class="abs fatwas" style="left:708px">
  <h2>New Fatwas</h2>
  <ul>
    <li>He works as a nurse, which means that he may do some things that are not acceptable according to sharee'ah.</li>
    <li class="hl">Her mother wants her to marry one suitor, but her father thinks that he is not suitable; what should she do?.</li>
    <li>Her mother wants her to marry one suitor, but her father thinks that he is not suitable; what should she do?.</li>
    <li class="hl">Raising Muslim children in the West to have an aversion to pigs.</li>
    <li>His parents think that he does not offer the naafil prayers, but he prays them in secret for fear of showing off. Should he tell them about that?.</li>
  </ul>
</section>

<div class="abs tabs" style="left:182px">
  <div class="tab big active" style="width:114px">Categories</div>
  <div class="tab big" style="width:64px">Files</div>
</div>
<section class="abs panel" style="left:182px">
  <ul>
    <li>Basic Tenets of Faith.</li>
    <li>The Quraan and its Sciences.</li>
    <li>Hadeeth &amp; its Sciences.</li>
    <li>Rulings on Jihaad.</li>
    <li>Fiqh of the family.</li>
    <li>Islamic history and biography.</li>
    <li>&nbsp;Enjoining what is good and forbidding what is evil.</li>
    <li>Pedagogy education and upbringing.</li>
    <li>Psychological and Social Problems.</li>
    <li>Islamic politics.</li>
  </ul>
</section>

<div class="abs tabs" style="left:607px">
  <div class="tab big" style="width:114px">Counselling</div>
  <div class="tab small" style="width:92px">Jurisprudence of<br>Acts of Worship</div>
  <div class="tab small active" style="width:97px">Jurisprudence of<br>Muslim Minorities</div>
</div>
<section class="abs panel right" style="left:607px">
  <ul>
    <li>They lived under Communist rule and did not know anything about praying and fasting; do they have to make it up?.</li>
    <li>They pray Jumu'ah in the workplace and do not go to the mosque.</li>
    <li>If some of the members of the congregation are praying outside the mosque and the power cuts out.</li>
    <li>Zakaah on monthly salaries and how is zakaah to be paid by one who is in debt?.</li>
  </ul>
</section>

<footer>
  <div class="abs rule-foot"></div>
  <p class="abs footer">All Rights Reserved for Tolvene Hub©&nbsp; 1997-2013&nbsp; 55.86</p>
</footer>

</body>
</html>
```